Law Firm Corporate Identity Package

Stationery, fax, and business card.
Updates

Name of firm is "Marwick Law PC."

Target Market(s)

Real estate investor clients

Industry/Entity Type

Legal

Font styles to use
Serif

Colors
3277b5
85acd3

```html
<!DOCTYPE html>
<html lang="en">
<head>
<meta charset="utf-8">
<title>Marwick Law PC — Corporate Identity</title>
<link href="https://fonts.googleapis.com/css2?family=Cinzel:wght@500&family=Jost:wght@400;600&display=swap" rel="stylesheet">
<style>
  :root {
    --brand-blue: #3277b5;
    --brand-light: #85acd3;
    --ink: #1d1d1d;
    --paper: #ffffff;
    --backdrop: #3a7dbd;
  }
  * { margin: 0; padding: 0; box-sizing: border-box; }
  html, body { width: 1200px; height: 1039px; overflow: hidden; }
  body { background: var(--backdrop); position: relative; font-family: "Jost", sans-serif; color: var(--ink); }

  .sheet { position: absolute; background: var(--paper); box-shadow: 0 4px 14px rgba(0,0,0,.35); overflow: hidden; }

  .brand-band { position: absolute; left: 0; right: 0; bottom: 0; display: flex; }
  .brand-band .band-blue { flex: 0 0 64%; background: linear-gradient(90deg, var(--brand-blue) 0%, var(--brand-light) 60%, var(--brand-blue) 100%); }
  .brand-band .band-black { flex: 1; background: linear-gradient(90deg, #000 0%, #555 45%, #000 100%); }

  .wordmark { position: absolute; display: flex; align-items: center; font-family: "Cinzel", serif; font-weight: 500; color: var(--ink); white-space: nowrap; }
  .wordmark .mark-square { background: var(--brand-blue); margin-right: .4em; flex: none; }

  .contact { position: absolute; line-height: 1.4; color: #333; }

  /* Letterhead */
  .letterhead { left: 48px; top: 133px; width: 553px; height: 781px; }
  .letterhead .wordmark { left: 16px; top: 28px; font-size: 28px; }
  .letterhead .wordmark .mark-square { width: 14px; height: 14px; }
  .letterhead .contact { left: 13px; top: 695px; font-size: 8.5px; }
  .letterhead .brand-band { height: 16px; }

  /* Business cards */
  .card { top: 162px; width: 206px; height: 133px; }
  .card .brand-band { height: 10px; }
  .card-front { left: 642px; }
  .card-front .wordmark { left: 0; right: 0; justify-content: center; top: 58px; font-size: 14px; }
  .card-front .wordmark .mark-square { width: 7px; height: 7px; }
  .card-back { left: 864px; }
  .card-back .wordmark { left: 7px; top: 16px; font-size: 12px; }
  .card-back .wordmark .mark-square { width: 6px; height: 6px; }
  .card-back .holder { position: absolute; right: 7px; top: 8px; text-align: right; }
  .card-back .holder-name { font-weight: 600; font-size: 10px; color: var(--brand-blue); letter-spacing: .2px; }
  .card-back .holder-role { font-size: 4.5px; color: #555; text-transform: uppercase; }
  .card-back .contact { left: 7px; top: 83px; font-size: 5.6px; line-height: 1.35; }

  /* Envelopes */
  .envelope { left: 637px; width: 529px; height: 238px; }
  .envelope-back { top: 372px; }
  .envelope-back .flap { position: absolute; left: 0; top: 0; width: 529px; height: 74px; }
  .envelope-front { top: 674px; }
  .envelope-front .wordmark { left: 8px; top: 14px; font-size: 15px; }
  .envelope-front .wordmark .mark-square { width: 8px; height: 8px; }
  .envelope-front .contact { left: 11px; top: 162px; font-size: 9px; }
  .envelope-front .brand-band { height: 8px; }
</style>
</head>
<body>

  <section class="sheet letterhead" aria-label="Letterhead">
    <div class="wordmark"><span class="mark-square"></span>Marwick Law PC</div>
    <address class="contact" style="font-style:normal">
      Marwick Law PC<br>Road, Area Name,<br>City, State. 00000<br>Phone: +1. 12345678<br>Fax: +1. 12345678
    </address>
    <div class="brand-band"><span class="band-blue"></span><span class="band-black"></span></div>
  </section>

  <section class="sheet card card-front" aria-label="Business card front">
    <div class="wordmark"><span class="mark-square"></span>Marwick Law PC</div>
    <div class="brand-band"><span class="band-blue"></span><span class="band-black"></span></div>
  </section>

  <section class="sheet card card-back" aria-label="Business card back">
    <div class="wordmark"><span class="mark-square"></span>Marwick Law PC</div>
    <div class="holder">
      <div class="holder-name">NAME HERE</div>
      <div class="holder-role">Designation</div>
    </div>
    <address class="contact" style="font-style:normal">
      Marwick Law PC<br>Road, Area Name,<br>City, State. 00000<br>Phone: +1. 12345678<br>Fax: +1. 12345678
    </address>
    <div class="brand-band"><span class="band-blue"></span><span class="band-black"></span></div>
  </section>

  <section class="sheet envelope envelope-back" aria-label="Envelope back">
    <svg class="flap" viewBox="0 0 529 74" aria-hidden="true">
      <path d="M0 0 H529 L509 60 Q504 74 488 74 H41 Q25 74 20 60 Z" fill="var(--brand-blue)"/>
    </svg>
  </section>

  <section class="sheet envelope envelope-front" aria-label="Envelope front">
    <div class="wordmark"><span class="mark-square"></span>Marwick Law PC</div>
    <address class="contact" style="font-style:normal">
      Marwick Law PC<br>Road, Area Name,<br>City, State. 00000<br>Phone: +1. 12345678<br>Fax: +1. 12345678
    </address>
    <div class="brand-band"><span class="band-blue"></span><span class="band-black"></span></div>
  </section>

</body>
</html>
```